Need to design a business card with logo

Hellow
we are a company ,
PT REKA LINTAS MANDIRI
looking for design of name card.
what we do is property development and management.
design preferable professional corporate look and feel.
corporate. color, pantone colour 289
information required is
company name " Reka Lintas Mandiri"
person name eg " Peter Hollis"
person title eg "secret agent"
address: 9 kestrel road , jakarta, indonesia
phone : +6221 5906471
mobile : 0813 294 615
email : peter@hollistran.com
website: www.peterhol.com
if you want to include logo in the design you are welcome and appreciated , or you can simply use the company name as the logo.
thanks
corporate , business person , show events, exhibition events ,etc
Business

```html
<!DOCTYPE html>
<html lang="en">
<head>
<meta charset="utf-8">
<title>Peter Hollis — Reka Lintas Mandiri Business Card</title>
<link rel="stylesheet" href="https://fonts.googleapis.com/css2?family=Macondo&display=swap">
<style>
  :root {
    --card-navy: #30357a;
    --card-navy-light: #3a4090;
    --card-navy-dark: #262a63;
    --ink: #07070f;
    --ink-shadow: rgba(0, 0, 0, 0.5);
    --ink-lift: rgba(120, 130, 210, 0.35);
  }
  html, body {
    margin: 0;
    padding: 0;
    width: 1200px;
    height: 480px;
    overflow: hidden;
    background: var(--card-navy);
  }
  .card {
    position: relative;
    width: 1200px;
    height: 480px;
    overflow: hidden;
    font-family: "Macondo", "Papyrus", fantasy;
    color: var(--ink);
    text-transform: uppercase;
  }
  .card__texture {
    position: absolute;
    inset: 0;
    background:
      radial-gradient(ellipse at 35% 40%, var(--card-navy-light) 0%, var(--card-navy) 55%, var(--card-navy-dark) 100%);
  }
  .company {
    position: absolute;
    right: 71px;
    top: 56px;
    margin: 0;
    font-size: 40px;
    font-weight: 400;
    letter-spacing: 2px;
    line-height: 1;
    text-shadow: 0 1px 1px var(--ink-lift);
  }
  .identity {
    position: absolute;
    left: 70px;
    bottom: 46px;
    display: flex;
    align-items: flex-end;
    gap: 10px;
  }
  .identity__line {
    writing-mode: vertical-rl;
    transform: rotate(180deg);
    line-height: 1;
    white-space: nowrap;
  }
  .identity__first,
  .identity__last {
    font-size: 64px;
    letter-spacing: -1px;
    text-shadow: 4px -4px 6px var(--ink-shadow);
  }
  .identity__title {
    font-size: 46px;
    letter-spacing: 2px;
    text-shadow: 3px -3px 5px var(--ink-shadow);
  }
  .contact {
    position: absolute;
    right: 71px;
    top: 232px;
    margin: 0;
    text-align: right;
    font-size: 39px;
    line-height: 36px;
    font-style: normal;
    letter-spacing: 0.5px;
    text-shadow: 0 1px 1px var(--ink-lift);
  }
  .contact__item {
    display: block;
    white-space: nowrap;
  }
</style>
</head>
<body>
  <main class="card">
    <div class="card__texture" role="img" aria-label="Subtle navy damask background pattern"></div>

    <h1 class="company">Reka Lintas Mandiri</h1>

    <div class="identity">
      <span class="identity__line identity__first">Peter</span>
      <span class="identity__line identity__last">Hollis</span>
      <span class="identity__line identity__title">Agent Secret</span>
    </div>

    <address class="contact">
      <span class="contact__item contact__web">www.peterhol.com</span>
      <span class="contact__item contact__address">9 kestrel road . Jakarta, Indonesia</span>
      <span class="contact__item contact__phone">+6221 5906471</span>
      <span class="contact__item contact__mobile">0813 294 615</span>
      <span class="contact__item contact__email">peter@hollistran.com</span>
    </address>
  </main>
</body>
</html>
```